Redesign of 3-4 page site for professional services firm

Our site is www.kestrelvaleadvisors.com. We currently have a simple page made with HostNimbo tools. But the tools are not able to generate the look and feel we desire. We need a home page similar to current that tells a little about our company, our experience and our team. We need a second page to show details of current and past transactions we have assisted our clients with. Currently this page reads like a word document but we would like for it to present in a cleaner fashion and liven it up with some images that link to the industry served. For example, a motorcycle outline in a circle for the powersports related transactions. We would like page to introduce each member of "Our Team" and highlight their experience with a photo of each person. If there is no photo available, we would like a placeholder to be their initials in a circle that can be updated later. We would also like a contact us section whether this is a different page or part of the home page.

Target Market(s)

Retirement minded business owners

Industry/Entity Type

Professional Services

Coding

Coded - Design and coding required

Requirements
Must have
• See project description. Must include a page or section for "Current Listings" and "Recently Completed Transactions" (can be same page)

```html
<!DOCTYPE html>
<html lang="en">
<head>
<meta charset="utf-8">
<title>Kestrel Vale Advisors</title>
<link href="https://fonts.googleapis.com/css2?family=Lexend:wght@300;400;500;600;700&display=swap" rel="stylesheet">
<style>
:root{
  --yellow:#fdf54a;
  --ink:#1d1d1f;
  --muted:#55575c;
  --gray:#f2f2f2;
  --dark:#2f3136;
  --white:#ffffff;
}
*{box-sizing:border-box;margin:0;padding:0}
html,body{width:1200px;height:3125px;overflow:hidden;background:var(--white)}
body{font-family:"Lexend",sans-serif;color:var(--ink);position:relative}
section,header,div{position:absolute}
.label{font-size:10px;font-weight:500;text-transform:uppercase;background:linear-gradient(transparent 55%,var(--yellow) 55%);padding:0 2px;letter-spacing:.2px}
.heading{font-size:23px;font-weight:500}
.body-text{font-size:9.5px;font-weight:300;line-height:16.4px;color:var(--muted)}
.btn{background:var(--yellow);font-size:9px;font-weight:500;text-transform:uppercase;display:flex;align-items:center;justify-content:center;color:var(--ink)}
.top-bar{left:0;top:0;width:1200px;height:22px;background:var(--yellow);font-size:8.5px;font-weight:400}
.top-bar span{position:absolute;top:5px;display:flex;align-items:center;gap:5px}
.nav{left:0;top:22px;width:1200px;height:58px;background:var(--white)}
.logo{font-size:16px;font-weight:500;display:flex;align-items:center;gap:6px}
.logo i{width:10px;height:10px;background:var(--yellow);display:block}
.nav-links{right:181px;top:24px;display:flex;gap:28px;font-size:9.5px;text-transform:uppercase}
.hero{left:0;top:80px;width:1200px;height:532px;background:linear-gradient(135deg,#3a3634,#1e1c1c 60%,#2a2522)}
.hero h1{font-size:39px;font-weight:700;color:var(--white);line-height:52px}
.hero h1 em{font-style:normal;color:var(--yellow)}
.band{left:0;top:612px;width:1200px;height:75px;background:var(--yellow)}
.photo{background:linear-gradient(135deg,#5b5652,#2d2b2a)}
.team-card{background:var(--yellow);border-radius:0 0 80px 80px;overflow:hidden}
.arrow-btn{width:27px;height:27px;background:var(--yellow);display:flex;align-items:center;justify-content:center}
.social{display:flex;gap:11px}
.social i{width:19px;height:19px;border-radius:50%;background:var(--ink);display:block}
.review{width:263px;height:166px;background:var(--white);border-radius:10px}
.review .avatar{left:19px;top:20px;width:50px;height:50px;border-radius:50%;background:#bdbdbd}
.review .role{left:82px;top:27px;font-size:7px;font-weight:500;text-transform:uppercase;background:linear-gradient(transparent 55%,var(--yellow) 55%)}
.review .name{left:82px;top:40px;font-size:11px;font-weight:500}
.review .quote{left:19px;top:88px;width:225px;font-size:9px;font-style:italic;font-weight:300;line-height:16px;color:var(--muted)}
.subscribe{left:0;top:2718px;width:1200px;height:209px;background:var(--dark)}
</style>
</head>
<body>

<header class="top-bar">
  <span style="left:181px">
    <svg width="8" height="10" viewBox="0 0 8 10"><path d="M4 0a4 4 0 0 1 4 4c0 3-4 6-4 6S0 7 0 4a4 4 0 0 1 4-4z" fill="#1d1d1f"/><circle cx="4" cy="4" r="1.5" fill="#fdf54a"/></svg>
    428 Alder Crest Road, Brightwater, Oklahoma 74120, United States
  </span>
  <span style="left:480px">
    <svg width="9" height="9" viewBox="0 0 10 10"><path d="M2 0l2 2.5-1.2 1.5a6 6 0 0 0 3.2 3.2L7.5 6 10 8l-1.5 2C4 10 0 6 0 1.5z" fill="#1d1d1f"/></svg>
    405-555-0182
  </span>
  <span style="right:181px;font-weight:600">GET STARTED TODAY! &#8594;</span>
</header>

<nav class="nav">
  <div class="logo" style="left:181px;top:18px"><i></i>Kestrel Vale</div>
  <div class="nav-links"><span>Home</span><span>Our Services</span><span>Business Listings</span><span>Our Team</span><span>Contact Us</span></div>
</nav>

<section class="hero">
  <svg width="1200" height="532" style="position:absolute;left:0;top:0">
    <path d="M1104 0 L1200 0 L1200 532 L740 532 C700 410 650 260 720 170 C800 80 950 55 1104 0 Z" fill="#7a6a5c" role="img" aria-label="Photo of a smiling business team shaking hands across a meeting table"/>
    <path d="M740 532 C700 410 650 260 720 170 C800 80 950 55 1104 0" fill="none" stroke="#fdf54a" stroke-width="9"/>
  </svg>
  <div style="left:181px;top:158px;font-size:12px;color:var(--white);border-bottom:2px solid #8a8640;padding-bottom:2px">WELCOME TO KESTREL VALE</div>
  <h1 style="position:absolute;left:181px;top:200px">Strategically <em>Navigating</em><br>Business Exits</h1>
  <div class="btn" style="left:181px;top:345px;width:88px;height:28px">Contact Us</div>
  <div style="left:287px;top:354px;font-size:9px;font-weight:500;color:var(--yellow)">Get Started Today &#8594;</div>
</section>

<div class="band"></div>

<section style="left:0;top:687px;width:1200px;height:520px">
  <div class="photo" style="left:0;top:75px;width:168px;height:168px" role="img" aria-label="Photo of two smiling colleagues in an office"></div>
  <div class="photo" style="left:186px;top:92px;width:168px;height:168px" role="img" aria-label="Photo of a smiling businessman"></div>
  <div class="photo" style="left:0;top:261px;width:168px;height:168px" role="img" aria-label="Photo of hands reviewing colourful charts"></div>
  <div class="photo" style="left:186px;top:276px;width:168px;height:168px" role="img" aria-label="Photo of a smiling woman at a laptop"></div>
  <div style="left:294px;top:230px;width:144px;height:76px;background:var(--white);border-radius:8px;display:flex;align-items:center;justify-content:center"><div class="logo" style="position:static"><i></i>Kestrel Vale</div></div>
  <div style="left:573px;top:133px"><span class="label">About Us</span></div>
  <div class="heading" style="left:573px;top:156px">Kestrel Vale Advisors</div>
  <p class="body-text" style="position:absolute;left:573px;top:211px;width:445px">At Kestrel Vale Advisors, our mission is to empower entrepreneurs and business owners by facilitating seamless transactions that lead to mutual success. We understand that selling or acquiring a business can be a complex and emotional journey, which is why our dedicated team of experts is here to guide you every step of the way.</p>
  <p class="body-text" style="position:absolute;left:573px;top:293px;width:445px">With a commitment to integrity, transparency, and unmatched professionalism, we strive to create a positive and rewarding experience for all our clients.</p>
  <div class="btn" style="left:573px;top:359px;width:87px;height:25px">Learn More</div>
</section>

<section style="left:0;top:1207px;width:1200px;height:448px;background:var(--gray)">
  <div style="left:181px;top:80px"><span class="label">Our Experience</span></div>
  <div class="heading" style="left:181px;top:104px">With Decades of Experience</div>
  <p class="body-text" style="position:absolute;left:181px;top:160px;width:445px">With decades of experience Kestrel Vale Advisors has proudly assisted numerous clients in successfully navigating the intricate journey of selling their businesses. Our team brings a wealth of knowledge and expertise acquired through years of working closely with entrepreneurs and business owners across diverse industries. We understand the unique challenges and complexities involved in selling a business, from valuation and marketing to negotiations and closing the deal.</p>
  <p class="body-text" style="position:absolute;left:181px;top:258px;width:445px">Our extensive experience allows us to anticipate potential obstacles and proactively find solutions, ensuring a seamless and efficient process for our clients. We take pride in our track record of delivering exceptional results and helping our clients achieve their desired outcomes.</p>
  <div class="btn" style="left:181px;top:340px;width:87px;height:24px">Learn More</div>
  <div style="left:693px;top:63px;width:314px;height:322px;background:var(--yellow)"></div>
  <div style="left:705px;top:75px;width:314px;height:310px;background:linear-gradient(160deg,#1f3a5c,#0d1a2c 60%,#2a3140)" role="img" aria-label="Photo of a hand typing on a laptop in front of stock market charts"></div>
  <div style="left:649px;top:37px;width:127px;height:127px;border-radius:50%;background:var(--yellow);display:flex;align-items:center;justify-content:center">
    <div style="position:static;width:111px;height:111px;border-radius:50%;background:var(--white);display:flex;flex-direction:column;align-items:center;justify-content:center">
      <span style="font-size:23px;font-weight:500">30+</span>
      <span style="font-size:8px;font-weight:500;margin-top:4px">YEARS EXPERIENCE</span>
    </div>
  </div>
</section>

<section style="left:0;top:1655px;width:1200px;height:669px">
  <div style="left:181px;top:72px"><span class="label">Our Team</span></div>
  <div class="heading" style="left:181px;top:96px">Meet Team Members</div>
  <div style="right:181px;top:108px;font-size:8.5px;font-weight:500">View All Members &#8594;</div>
  <div class="arrow-btn" style="left:432px;top:273px"><svg width="12" height="10" viewBox="0 0 12 10"><path d="M11 5H2M5 1L1 5l4 4" stroke="#1d1d1f" stroke-width="2" fill="none"/></svg></div>
  <div class="arrow-btn" style="left:740px;top:273px"><svg width="12" height="10" viewBox="0 0 12 10"><path d="M1 5h9M7 1l4 4-4 4" stroke="#1d1d1f" stroke-width="2" fill="none"/></svg></div>
  <div class="team-card" style="left:484px;top:155px;width:231px;height:262px">
    <div style="left:35px;top:30px;width:161px;height:232px;border-radius:80px 80px 0 0;background:linear-gradient(#c8b39a,#2b3244 70%)" role="img" aria-label="Portrait photo of team member Daniel Hartwell in a suit"></div>
  </div>
  <div style="left:0;width:1200px;top:441px;text-align:center;font-size:14px;font-weight:500">Daniel Hartwell, CPA, JD</div>
  <p class="body-text" style="position:absolute;left:300px;top:474px;width:600px;text-align:center">Daniel is a forward thinking Certified Public Accountant and JD, blending business, finance and legal expertise to help clients reach their short and long term goals. In addition to the public practice of law and accounting (including implementing advanced tax planning strategies), Daniel has a record of establishing sustainable start-up operations, introducing new products and developing innovative sales and marketing techniques. Daniel has also assisted and advised many clients on the sale of their business. This experience allows Daniel to provide exceptional value to Kestrel Vale clients, their families, and their businesses.</p>
  <div class="social" style="left:545px;top:574px"><i></i><i></i><i></i><i></i></div>
</section>

<section style="left:0;top:2324px;width:1200px;height:394px;background:var(--gray);overflow:hidden">
  <div style="left:0;width:1200px;top:50px;text-align:center"><span class="label">Reviews</span></div>
  <div class="heading" style="left:0;width:1200px;top:77px;text-align:center">What They Say About Us</div>
  <div class="review" style="left:-106px;top:130px;opacity:.45"><div class="avatar"></div><div class="role">Journalist</div><div class="name">Daniel Hartwell, CPA, JD</div><div class="quote">“With decades of experience Kestrel Vale Advisors has proudly assisted numerous clients in successfully navigating the intricate journey of selling their businesses.”</div></div>
  <div class="review" style="left:181px;top:130px"><div class="avatar"></div><div class="role">Journalist</div><div class="name">Daniel Hartwell, CPA, JD</div><div class="quote">“With decades of experience Kestrel Vale Advisors has proudly assisted numerous clients in successfully navigating the intricate journey of selling their businesses.”</div></div>
  <div class="review" style="left:468px;top:130px"><div class="avatar"></div><div class="role">Journalist</div><div class="name">Daniel Hartwell, CPA, JD</div><div class="quote">“With decades of experience Kestrel Vale Advisors has proudly assisted numerous clients in successfully navigating the intricate journey of selling their businesses.”</div></div>
  <div class="review" style="left:756px;top:130px"><div class="avatar"></div><div class="role">Journalist</div><div class="name">Daniel Hartwell, CPA, JD</div><div class="quote">“With decades of experience Kestrel Vale Advisors has proudly assisted numerous clients in successfully navigating the intricate journey of selling their businesses.”</div></div>
  <div class="review" style="left:1043px;top:130px;opacity:.45"><div class="avatar"></div><div class="role">Journalist</div><div class="name">Daniel Hartwell, CPA, JD</div><div class="quote">“With decades of experience Kestrel Vale Advisors has proudly assisted numerous clients in successfully navigating the intricate journey of selling their businesses.”</div></div>
  <div style="left:578px;top:327px;width:12px;height:2px;background:#bdbdbd"></div>
  <div style="left:594px;top:327px;width:12px;height:3px;background:var(--ink)"></div>
  <div style="left:610px;top:327px;width:12px;height:2px;background:#bdbdbd"></div>
</section>

<section class="subscribe">
  <svg width="520" height="209" style="position:absolute;left:0;top:0">
    <path d="M0 0 L300 0 C420 20 480 120 510 209 L0 209 Z" fill="#9a9ea3" role="img" aria-label="Photo of a modern office with desks, chairs and computer monitors"/>
    <path d="M300 0 C420 20 480 120 510 209" fill="none" stroke="#fdf54a" stroke-width="9"/>
  </svg>
  <div style="left:618px;top:51px"><span class="label" style="color:var(--white);background:linear-gradient(transparent 55%,#8a8a2a 55%)">Subscribe</span></div>
  <div style="left:618px;top:72px;font-size:23px;font-weight:500;color:var(--white)">Sign Up to <span style="color:var(--yellow)">Hear</span> From Us</div>
  <div style="left:619px;top:127px;width:397px;height:31px;background:#3e4046;border-radius:3px">
    <div style="left:12px;top:10px;font-size:8.5px;color:#d8d8d8;font-weight:300">Enter your email address here...</div>
    <div class="btn" style="right:3px;top:3px;width:82px;height:25px">Sign Up &#8594;</div>
  </div>
</section>

<div style="left:181px;top:3003px;width:838px;height:122px;border-radius:10px 10px 0 0;background:linear-gradient(135deg,#d6ecdf,#c4e2d6 60%,#d9eedf)" role="img" aria-label="Map showing the office location and surrounding area"></div>

</body>
</html>
```